Produktblatt für Anbieter von Nahrungsergänzungsmitteln
Zielgruppe
Nahrungsergänzungsmittel für medizinische Zwecke, insbesondere in Pulver- und Pastillenform auf
pflanzlicher Basis mit Getreide- und Kräuterinhaltsstoffen
Mehlmischung zum Kochen und Backen, Nudeln, Teig, Teigwaren, Kuchen, Torten, usw.
Aufgabenstellung
Naturverbundenheit, Logo, font Avenir Next LT Pro, ansprechend online und ausgedruckt, textliche Inhalte

```html
<!DOCTYPE html>
<html lang="de">
<head>
<meta charset="utf-8">
<title>Vollkorngetreide – Produktblatt</title>
<link href="https://fonts.googleapis.com/css2?family=Figtree:wght@400;600;700;800;900&display=swap" rel="stylesheet">
<style>
  :root{
    --stage:#f2f2f2;
    --paper:#ffffff;
    --orange:#ff9f0a;
    --pill:#fdbf5a;
    --green:#2e8b1f;
    --green-light:#62bd2e;
    --ink:#1d1d1d;
    --leaf-soft:#cfe8c4;
    --grass:#6f8f3a;
  }
  *{box-sizing:border-box;margin:0;padding:0}
  html,body{width:1200px;height:1200px;overflow:hidden;background:var(--stage);font-family:"Figtree",sans-serif}
  .sheet{position:absolute;left:188px;top:0;width:825px;height:1200px;background:var(--paper);overflow:hidden;color:var(--ink)}
  .abs{position:absolute}

  .leaves{position:absolute;border-radius:50%;opacity:.8}
  .leaves--top{left:545px;top:37px;width:300px;height:254px;background:radial-gradient(ellipse at 60% 50%,#7fbf5e 0%,#b8dca6 45%,rgba(255,255,255,0) 72%)}
  .leaves--left{left:-30px;top:722px;width:260px;height:330px;background:radial-gradient(ellipse at 50% 55%,#8fca72 0%,#c6e4b8 45%,rgba(255,255,255,0) 72%)}
  .leaves--right{left:575px;top:790px;width:270px;height:260px;background:radial-gradient(ellipse at 60% 55%,#8fca72 0%,#c6e4b8 45%,rgba(255,255,255,0) 72%)}

  .title{left:81px;top:96px;font-size:40px;line-height:41px;font-weight:900;color:var(--orange);letter-spacing:.2px}
  .title-rule{left:0;top:190px;width:224px;height:6px;background:var(--orange)}
  .intro{left:83px;top:230px;font-size:19.5px;line-height:23px;color:var(--orange);font-weight:400}

  .col-left{left:83px;top:342px;width:320px}
  .col-right{left:429px;top:344px;width:330px}
  .lead{font-size:16.5px;line-height:20px;font-weight:800;color:var(--green);margin-bottom:10px}
  .heading{font-size:19px;line-height:22px;font-weight:800;color:var(--green);margin-bottom:10px}
  .body{font-size:16px;line-height:20px;font-weight:400}
  .body + .body{margin-top:10px}

  .uses{left:81px;top:547px;width:320px}
  .uses ul{list-style:none;margin-top:12px}
  .uses li{font-size:16px;line-height:20px;padding-left:10px;text-indent:-10px;margin-bottom:11px}
  .uses li::before{content:"• ";}

  .pill{position:absolute;right:0;height:34px;background:var(--pill);border-radius:17px 0 0 17px;display:flex;align-items:center;padding-left:14px;color:#fff;font-weight:700;font-size:14px}
  .pill svg{width:21px;height:21px;margin-right:20px;flex:none}

  .disclaimer{left:411px;top:773px;width:370px;font-size:9px;line-height:12.5px;color:var(--green)}

  .photo{position:absolute}
  .photo--person{left:231px;top:831px;width:225px;height:212px;background:linear-gradient(180deg,#e9e4df 0%,#f3efec 55%,#d9c4b0 100%);border-radius:100px 100px 0 0}
  .photo--meadow{left:0;top:1043px;width:825px;height:157px;background:linear-gradient(180deg,#a5b98a 0%,#7d9b4a 45%,#5b7a2c 100%)}
  .bottom-rule{left:532px;top:1162px;width:293px;height:5px;background:var(--orange)}

  .seal{left:415px;top:828px;width:164px;height:164px;border-radius:50%;background:linear-gradient(160deg,var(--green-light),#2d8a1e);color:#fff;text-align:center;display:flex;flex-direction:column;justify-content:center}
  .seal strong{font-size:22px;line-height:25px;font-weight:800}
  .seal span{font-size:11.5px;font-weight:600;margin-top:3px}
</style>
</head>
<body>
<main class="sheet">
  <div class="leaves leaves--top" role="img" aria-label="Gezeichnete grüne Blattranke"></div>
  <div class="leaves leaves--left" role="img" aria-label="Gezeichnete grüne Blattranken"></div>
  <div class="leaves leaves--right" role="img" aria-label="Gezeichnete grüne Blattranken"></div>

  <h1 class="abs title">VOLLKORNGETREIDE<br>IST LEBENSNOTWENDIG</h1>
  <div class="abs title-rule"></div>

  <p class="abs intro">Es ist der größte Vitamin B-Komplex Lieferant vor allem Vitamin B1 – es<br>enthält alle uns bekannten Vitalstoffe und auch jene noch nicht erforsch-<br>ten unbekannten und ist ein wichtiger Eiweißlieferant (pflanzlich).</p>

  <section class="abs col-left">
    <h2 class="lead">Die Presslinge haben eine<br>Durchblutungsfördernde und<br>Stoffwechselaktivierende Wirkung.</h2>
    <p class="body">Unterstützen die Darmaktivität mit vielen wichtigen Vitalstoffen welche natürliche Inhaltsstoffe der Bestandteile sind.<br>Durch die hohe Quelleigenschaft kann ein vermindertes Hungergefühl auftreten.</p>
  </section>

  <section class="abs col-right">
    <h2 class="heading">Vitamin C</h2>
    <p class="body">Unterstützen die Darmaktivität mit vielen wichtigen Vitalstoffen welche natürliche Inhaltsstoffe der Bestandteile sind.</p>
    <p class="body">Durch die hohe Quelleigenschaft kann<br>ein vermindertes Hungergefühl auftreten.</p>
  </section>

  <section class="abs uses">
    <h2 class="heading">Einsatzmöglichkeiten</h2>
    <ul>
      <li>Steigerung der Leistung und der Fitness</li>
      <li>Förderung der Gesundheit und des Wohlbefindens</li>
      <li>Minderung des Hungergefühls</li>
      <li>Optimaler Wachstum und gesunde Entwicklung der Kinder</li>
      <li>Muskel und Kraftaufbau</li>
    </ul>
  </section>

  <div class="pill" style="top:513px;width:350px">
    <svg viewBox="0 0 24 24"><circle cx="12" cy="12" r="11" fill="#3aa33a"/><circle cx="12" cy="12" r="7" fill="none" stroke="#fff" stroke-width="1.5"/><path d="M12 16V9M12 12l-3-2M12 12l3-2" stroke="#fff" stroke-width="1.5" fill="none"/></svg>
    Nach dem Reinsubstanzenprinzip
  </div>
  <div class="pill" style="top:556px;width:364px">
    <svg viewBox="0 0 24 24"><circle cx="12" cy="12" r="10" fill="none" stroke="#f08a00" stroke-width="1.5"/><path d="M5 5l14 14" stroke="#f08a00" stroke-width="1.5"/></svg>
    Frei von Zusatzstoffen
  </div>
  <div class="pill" style="top:600px;width:378px">
    <svg viewBox="0 0 24 24"><circle cx="12" cy="12" r="10" fill="none" stroke="#f08a00" stroke-width="1.5"/><path d="M5 5l14 14M9 15l3-7 3 7" stroke="#f08a00" stroke-width="1.5" fill="none"/></svg>
    Ohne Farb-, Geschmacks &amp; Überzugsstoffe
  </div>
  <div class="pill" style="top:643px;width:392px">
    <svg viewBox="0 0 24 24"><circle cx="12" cy="12" r="10" fill="none" stroke="#f08a00" stroke-width="1.5"/><path d="M12 6v12M9 9l3 2 3-2M9 13l3 2 3-2" stroke="#f08a00" stroke-width="1.5" fill="none"/></svg>
    Glutenfrei, Lactosefrei &amp; Fructosefrei
  </div>
  <div class="pill" style="top:687px;width:406px">
    <svg viewBox="0 0 24 24"><circle cx="12" cy="12" r="10" fill="none" stroke="#3aa33a" stroke-width="1.5"/><path d="M8 15c0-5 4-7 8-7-1 5-4 7-8 7z" stroke="#3aa33a" stroke-width="1.5" fill="none"/></svg>
    100% vegetarisch
  </div>
  <div class="pill" style="top:730px;width:420px">
    <svg viewBox="0 0 24 24"><circle cx="12" cy="12" r="10" fill="none" stroke="#3aa33a" stroke-width="1.5"/><path d="M12 6c3 4 4 6 4 8a4 4 0 0 1-8 0c0-2 1-4 4-8z" stroke="#3aa33a" stroke-width="1.5" fill="none"/></svg>
    Hypoallergen
  </div>

  <p class="abs disclaimer">Die Kornquell-Produkten sollten nicht als Ersatz für eine ausgewogene und abwechslungsreiche Ernährung verwendet werden.Die angegebene empfohlene tägliche Verzehrsmenge darf nicht überschritten werden.</p>

  <div class="photo photo--meadow" role="img" aria-label="Foto einer sonnigen Wiese im Park"></div>
  <div class="photo photo--person" role="img" aria-label="Foto einer lächelnden Frau im weißen Hemd mit ausgebreiteten Armen"></div>
  <div class="abs bottom-rule"></div>

  <div class="abs seal"><strong>Geprüfte<br>Qualität</strong><span>für Ihr Wohlbefinden!</span></div>
</main>
</body>
</html>
```